Business Card Design

i am looking a business card for a car rental company long with Taxi service also a logo.
Updates

what is the latest with my project

Industry/Entity Type

Business

Contact Information for Business Card

name of the Company is Brenmoor Auto Hire and Cab Services
Address: Cedar Hill Village, St. Anne's Parish Antigua
Tele# 558-2047/6194852-613-9075
Email: tolvipark@quenmail.net

Font styles to use
Script

```html
<!DOCTYPE html>
<html lang="en">
<head>
<meta charset="utf-8">
<title>Brenmoor Auto Hire and Cab Services – Business Card</title>
<link href="https://fonts.googleapis.com/css2?family=Arimo:wght@400;700&display=swap" rel="stylesheet">
<style>
  :root {
    --backdrop: #8e0029;
    --card-black: #1f1d1d;
    --taxi-yellow: #f2cd1f;
    --taxi-yellow-deep: #e4bc16;
    --ink: #1c1a1a;
    --contact-yellow: #f0c31a;
  }
  html, body {
    margin: 0;
    width: 1200px;
    height: 887px;
    overflow: hidden;
    background: var(--backdrop);
  }
  .card {
    position: absolute;
    left: 170px;
    top: 193px;
    width: 860px;
    height: 500px;
    border-radius: 44px;
    overflow: hidden;
    background: var(--card-black);
    font-family: "Arimo", Arial, sans-serif;
  }
  .contact {
    position: absolute;
    top: 34px;
    left: 0;
    right: 0;
    text-align: center;
    color: var(--contact-yellow);
  }
  .contact-item {
    display: flex;
    flex-direction: column;
    align-items: center;
    margin-bottom: 14px;
  }
  .contact-icon {
    width: 30px;
    height: 30px;
    margin-bottom: 8px;
  }
  .contact-text {
    font-size: 24px;
    letter-spacing: 0.5px;
  }
  .address .contact-text { font-size: 21px; }
  .brand-band {
    position: absolute;
    left: 0;
    right: 0;
    bottom: 0;
    height: 200px;
    background: linear-gradient(100deg, var(--taxi-yellow) 0%, var(--taxi-yellow-deep) 50%, var(--taxi-yellow) 100%);
  }
  .brand-name {
    position: absolute;
    left: 30px;
    top: 12px;
    margin: 0;
    font-size: 112px;
    font-weight: 700;
    letter-spacing: -3px;
    line-height: 1;
    color: var(--ink);
  }
  .brand-services {
    position: absolute;
    left: 34px;
    top: 124px;
    margin: 0;
    font-size: 50px;
    font-weight: 400;
    line-height: 1;
    color: var(--ink);
  }
</style>
</head>
<body>
  <div class="card">
    <div class="contact">
      <div class="contact-item phone">
        <svg class="contact-icon" viewBox="0 0 30 30" aria-hidden="true">
          <circle cx="15" cy="15" r="15" fill="var(--contact-yellow)"/>
          <path d="M10 8.5c.6-.6 1.5-.5 1.9.2l1.5 2.4c.3.5.2 1.2-.2 1.6l-1 1c.8 1.7 2.2 3.1 3.9 3.9l1-1c.4-.4 1.1-.5 1.6-.2l2.4 1.5c.7.4.8 1.3.2 1.9l-1.1 1.1c-1 1-3.5.9-6.5-2.1S8 10.6 9 9.6z" fill="var(--card-black)"/>
        </svg>
        <span class="contact-text">558-2047 / 6194852-613-9075</span>
      </div>
      <div class="contact-item email">
        <svg class="contact-icon" viewBox="0 0 30 30" aria-hidden="true">
          <circle cx="15" cy="15" r="15" fill="var(--contact-yellow)"/>
          <rect x="8" y="10" width="14" height="10" rx="1" fill="var(--card-black)"/>
          <path d="M8.5 10.5 15 15.5l6.5-5" fill="none" stroke="var(--contact-yellow)" stroke-width="1.3"/>
        </svg>
        <span class="contact-text">tolvipark@quenmail.net</span>
      </div>
      <div class="contact-item address">
        <svg class="contact-icon" viewBox="0 0 30 30" aria-hidden="true">
          <circle cx="15" cy="15" r="15" fill="var(--contact-yellow)"/>
          <path d="M15 7a5.5 5.5 0 0 0-5.5 5.5C9.5 17 15 23 15 23s5.5-6 5.5-10.5A5.5 5.5 0 0 0 15 7z" fill="var(--card-black)"/>
          <circle cx="15" cy="12.5" r="2" fill="var(--contact-yellow)"/>
        </svg>
        <span class="contact-text">Cedar Hill Village, St. Anne's Parish Antigua</span>
      </div>
    </div>

    <div class="brand-band" role="img" aria-label="Yellow taxi checkerboard pattern band">
      <p class="brand-name">BRENMOOR</p>
      <p class="brand-services">Auto Hire and CAB Services</p>
    </div>
  </div>
</body>
</html>
```